5-star Hotel Web Design Project

I need a custom website design for a 5-star hotel. For full details please look at the attached ZIP archive.

The design should be in layers in Photoshop/Illustrator/InDesign format with all the icons/shapes/maps/graphic assets in vector format (svg, ai, eps) as much as possible.

I prefer white, simple but elegant websites. Please consider the performance/coding experience. We're not making something to show off our design skills on a design contest with fancy parallax effects and confusing animations. We're trying to create usable, functional and clean UI with good UX.

I would like to receive a few option for the color scheme to choose from.

The website will be custom coded, i.e. I'm not using WordPress.

NOTE: Don't bother to submit the generic WordPress style templates. We're looking for something custom made with attention to details. That's why the price is not guaranteed, but don't be mistaken, I'm a long time buyer here on SketchHive and all my projects are paid in full.

Low design quality

Europe

Hotel

5+ page

```html
<!DOCTYPE html>
<html lang="en">
<head>
<meta charset="utf-8">
<title>Location – Duskfall Resort</title>
<link href="https://fonts.googleapis.com/css2?family=Montserrat:wght@400;500;600;700&display=swap" rel="stylesheet">
<style>
:root{
  --gold:#d3a96a;
  --brand:#b3262c;
  --ink:#222;
  --text:#6d6d6d;
  --muted:#8a8a8a;
  --band:#f2f2f2;
  --line:#e4e4e4;
}
*{box-sizing:border-box;margin:0;padding:0}
html,body{width:1200px;height:3863px;overflow:hidden}
body{font-family:"Montserrat",sans-serif;color:var(--ink);background:#fff;position:relative}
.wrap{width:978px;margin:0 auto;position:relative}
.site-header{height:130px}
.brand{position:absolute;left:0;top:40px;display:flex;align-items:center;gap:10px}
.brand-mark{width:26px;height:26px;border-radius:50%;background:var(--brand)}
.brand-name{font-size:26px;font-weight:600;color:var(--brand);line-height:1}
.topbar{position:absolute;right:0;top:24px;font-size:17px;display:flex;align-items:center;gap:10px;color:var(--ink)}
.topbar svg{width:14px;height:14px;fill:var(--gold)}
.flag{display:inline-block;width:24px;height:14px;background:#1d3f8f;position:relative;vertical-align:middle}
.flag::before{content:"";position:absolute;left:0;right:0;top:5px;height:4px;background:#d22}
.flag::after{content:"";position:absolute;top:0;bottom:0;left:10px;width:4px;background:#d22}
.caret{border:5px solid transparent;border-top-color:#444;display:inline-block;margin-top:5px}
.main-nav{position:absolute;right:0;top:78px;display:flex;gap:35px;font-size:17px;font-weight:600;letter-spacing:.3px}
.main-nav a{color:var(--ink);text-decoration:none}
.main-nav a.current{color:var(--gold)}
.intro{background:var(--band);height:635px;text-align:center;padding-top:38px}
.intro h1{font-size:50px;font-weight:700;letter-spacing:1px;margin-bottom:26px}
.intro p{width:930px;margin:0 auto 27px;font-size:16px;line-height:26.5px;color:var(--text)}
.gallery{position:absolute;top:830px;left:111px;width:978px;height:660px}
.ph{position:absolute}
.g1{left:0;top:0;width:312px;height:315px;background:linear-gradient(160deg,#9fb0b4,#c9cfc8 55%,#6aa1b8)}
.g2{left:326px;top:0;width:312px;height:315px;background:linear-gradient(170deg,#8fb6cf,#6f7f6a 50%,#8fa7a8)}
.g3{left:652px;top:0;width:312px;height:211px;background:linear-gradient(180deg,#2e6a72,#1f3a52 60%,#6a5330)}
.g4{left:652px;top:224px;width:312px;height:211px;background:linear-gradient(160deg,#c9cbcc,#eef0f0 60%,#a9aeaf)}
.g5{left:0;top:328px;width:638px;height:332px;background:linear-gradient(180deg,#3c7fc6,#c8d9ea 45%,#2f7fb8 58%,#1a5f93)}
.g6{left:652px;top:448px;width:312px;height:212px;background:linear-gradient(180deg,#e9a88f,#f1b89a 50%,#8a6a6a)}
.landmarks-title{position:absolute;top:1598px;left:0;width:1200px;text-align:center;font-size:35px;font-weight:500}
.cards{position:absolute;top:1677px;left:111px;width:978px;display:grid;grid-template-columns:repeat(3,314px);column-gap:18px;row-gap:18px}
.card{height:410px;border:1px solid var(--line);border-radius:4px;box-shadow:0 2px 6px rgba(0,0,0,.06);text-align:center;position:relative;background:#fff}
.card .ph{position:static;height:208px;border-radius:3px 3px 0 0}
.card h3{font-size:21px;font-weight:500;line-height:25px;height:58px;display:flex;align-items:center;justify-content:center;padding:0 10px;margin-top:8px}
.card p{font-size:15px;line-height:25px;color:var(--muted);padding:0 30px}
.card .foot{position:absolute;left:18px;right:18px;bottom:18px;display:flex;align-items:center;justify-content:space-between}
.dist{font-size:15px;color:#555}
.dist b{font-weight:700;color:var(--ink)}
.btn{background:var(--gold);color:#fff;font-size:17px;font-weight:600;padding:11px 10px;width:147px;text-align:center;text-decoration:none;letter-spacing:.3px}
.t-snow{background:linear-gradient(180deg,#b9bcbd,#e4e5e5 60%,#8a8c8e)}
.t-pool{background:linear-gradient(180deg,#2b3d52,#1c4f8b 55%,#0f2d63)}
.t-slide{background:linear-gradient(180deg,#86b4df,#e7dcc8 55%,#d14a2e)}
.t-dusk{background:linear-gradient(180deg,#6c7f92,#8ca0b3 50%,#2e3b46)}
.t-night{background:linear-gradient(180deg,#3c3426,#9a7a3e 55%,#3f6a2b)}
.t-facade{background:linear-gradient(180deg,#a8c9de,#e6e3de 55%,#8f8573)}
.t-lamp{background:linear-gradient(180deg,#5a4020,#3a2a16 55%,#4a6e1e)}
.t-grey{background:linear-gradient(180deg,#9a9d98,#bfb39a 55%,#7b6e56)}
.site-footer{position:absolute;top:3445px;left:0;width:1200px;height:418px;background:#f3f3f3}
.f-brand{position:absolute;left:108px;top:70px;display:flex;align-items:center;gap:10px}
.f-contact{position:absolute;left:111px;top:160px;font-size:15px;color:#555;line-height:20px}
.f-contact li{list-style:none;display:flex;gap:8px;margin-bottom:18px}
.f-contact svg{width:13px;height:13px;fill:var(--gold);flex:none;margin-top:3px}
.f-col{position:absolute;top:60px}
.f-col h4{font-size:21px;font-weight:500;margin-bottom:14px}
.f-col ul{list-style:none;display:grid;grid-template-columns:repeat(2,auto);column-gap:26px;row-gap:13px;font-size:15px;color:#555}
.f-col.legal ul{grid-template-columns:auto}
.rule{position:absolute;left:111px;right:111px;top:315px;border-top:1px solid #ddd}
.copy{position:absolute;left:111px;top:357px;font-size:15px;color:#555}
.social{position:absolute;right:111px;top:340px;display:flex;gap:10px}
.social span{width:41px;height:41px;border:2px solid var(--brand);border-radius:50%}
</style>
</head>
<body>
<header class="site-header wrap">
  <div class="brand"><span class="brand-mark"></span><span class="brand-name">Duskfall Resort</span></div>
  <div class="topbar">
    <svg viewBox="0 0 24 24"><path d="M6.6 10.8a15 15 0 006.6 6.6l2.2-2.2c.3-.3.7-.4 1-.2 1.1.4 2.3.6 3.6.6.6 0 1 .4 1 1V20c0 .6-.4 1-1 1A17 17 0 013 4c0-.6.4-1 1-1h3.5c.6 0 1 .4 1 1 0 1.3.2 2.5.6 3.6.1.3 0 .7-.2 1z"/></svg>
    <span>+990 500 123 45</span><span>|</span>
    <svg viewBox="0 0 24 24"><path d="M2 5h20v14H2zm2 2v.5l8 5 8-5V7z"/></svg>
    <span>stay@duskfallresort.example</span><span>|</span>
    <span class="flag"></span><span>English</span><span class="caret"></span>
  </div>
  <nav class="main-nav">
    <a href="#">DUSKFALL RESORT</a><a href="#">BOOK DIRECT</a><a href="#">SPECIAL OFFERS</a><a href="#" class="current">LOCATION</a>
  </nav>
</header>

<section class="intro">
  <h1>LOCATION</h1>
  <p>At vero eos et accusamus et iusto odio dignissimos ducimus qui blanditiis praesentium voluptatum deleniti atque corrupti quos dolores et quas molestias excepturi sint occaecati cupiditate non provident, similique sunt in culpa qui officia deserunt mollitia animi, id est laborum et dolorum fuga.</p>
  <p>Et harum quidem rerum facilis est et expedita distinctio. Nam libero tempore, cum soluta nobis est eligendi optio cumque nihil impedit quo minus id quod maxime placeat facere possimus, omnis voluptas assumenda est, omnis dolor repellendus. Temporibus autem quibusdam et aut officiis debitis aut rerum necessitatibus saepe eveniet ut et voluptates repudiandae sint et molestiae non recusandae.</p>
  <p>Nemo enim ipsam voluptatem quia voluptas sit aspernatur aut odit aut fugit, sed quia consequuntur magni dolores eos qui ratione voluptatem sequi nesciunt. Neque porro quisquam est, qui dolorem ipsum quia dolor sit amet, consectetur, adipisci velit, sed quia non numquam eius modi tempora incidunt ut labore et dolore magnam aliquam quaerat voluptatem.</p>
  <p>Ut enim ad minima veniam, quis nostrum exercitationem ullam corporis suscipit laboriosam, nisi ut aliquid ex ea commodi consequatuNemo enim ipsam voluptatem quia voluptas sit aspernatur aut odit aut fugit, sed quia co nsequuntur magni dolores eos qui ratione voluptatem sequi nesciunt</p>
</section>

<section class="gallery">
  <div class="ph g1" role="img" aria-label="Aerial view of the resort with pools beside the beach"></div>
  <div class="ph g2" role="img" aria-label="Resort buildings and pool seen from above with the sea behind"></div>
  <div class="ph g3" role="img" aria-label="Main entrance canopy of the resort at dusk"></div>
  <div class="ph g4" role="img" aria-label="Resort grounds covered in snow"></div>
  <div class="ph g5" role="img" aria-label="Resort skyline seen from the sea under a blue sky"></div>
  <div class="ph g6" role="img" aria-label="Sunset over the bay with the resort on the horizon"></div>
</section>

<h2 class="landmarks-title">NEARBY LANDMARKS</h2>
<section class="cards">
  <article class="card"><div class="ph t-snow" role="img" aria-label="Snowy rooftop terrace with a domed building"></div><h3>Monastery of the Cliffs</h3><p>Lorem ipsum dolor sit amet, cons ecte tur adipiscing elied do.</p><div class="foot"><span class="dist">Up to <b>2</b> km</span><a class="btn" href="#">LEARN MORE</a></div></article>
  <article class="card"><div class="ph t-pool" role="img" aria-label="Illuminated pool at night"></div><h3>Saltmere Lake</h3><p>Lorem ipsum dolor sit amet, cons ecte tur adipiscing elied do.</p><div class="foot"><span class="dist">Up to <b>2</b> km</span><a class="btn" href="#">LEARN MORE</a></div></article>
  <article class="card"><div class="ph t-slide" role="img" aria-label="Colourful water slides in front of the resort"></div><h3>Duskfall Aquapark Saltmere</h3><p>Lorem ipsum dolor sit amet, cons ecte tur adipiscing elied do.</p><div class="foot"><span class="dist">Up to <b>2</b> km</span><a class="btn" href="#">LEARN MORE</a></div></article>
  <article class="card"><div class="ph t-dusk" role="img" aria-label="Resort building facade at dusk"></div><h3>Old Necropolis Saltmere</h3><p>Lorem ipsum dolor sit amet, cons ecte tur adipiscing elied do.</p><div class="foot"><span class="dist">Up to <b>2</b> km</span><a class="btn" href="#">LEARN MORE</a></div></article>
  <article class="card"><div class="ph t-night" role="img" aria-label="Lit promenade in front of the resort at night"></div><h3>Embankment</h3><p>Lorem ipsum dolor sit amet, cons ecte tur adipiscing elied do.</p><div class="foot"><span class="dist">Up to <b>2</b> km</span><a class="btn" href="#">LEARN MORE</a></div></article>
  <article class="card"><div class="ph t-facade" role="img" aria-label="Resort building with arched balconies"></div><h3>Museum of Brine</h3><p>Lorem ipsum dolor sit amet, cons ecte tur adipiscing elied do.</p><div class="foot"><span class="dist">Up to <b>2</b> km</span><a class="btn" href="#">LEARN MORE</a></div></article>
  <article class="card"><div class="ph t-lamp" role="img" aria-label="Lamp-lit garden beside the resort at night"></div><h3>Old Houses of Saltmere architectural reserve</h3><p>Lorem ipsum dolor sit amet, cons ecte tur adipiscing elied do.</p><div class="foot"><span class="dist">Up to <b>2</b> km</span><a class="btn" href="#">LEARN MORE</a></div></article>
  <article class="card"><div class="ph t-grey" role="img" aria-label="Resort buildings with rounded balconies"></div><h3>Saltmere Museum of History</h3><p>Lorem ipsum dolor sit amet, cons ecte tur adipiscing elied do.</p><div class="foot"><span class="dist">Up to <b>2</b> km</span><a class="btn" href="#">LEARN MORE</a></div></article>
  <article class="card"><div class="ph t-night" role="img" aria-label="Resort gardens lit up in the evening"></div><h3>Street Market in Brinevo on Thursday</h3><p>Lorem ipsum dolor sit amet, cons ecte tur adipiscing elied do.</p><div class="foot"><span class="dist">Up to <b>2</b> km</span><a class="btn" href="#">LEARN MORE</a></div></article>
  <article class="card"><div class="ph t-lamp" role="img" aria-label="Lamp-lit garden beside the resort at night"></div><h3>Saltmere Lake Visitor Centre</h3><p>Lorem ipsum dolor sit amet, cons ecte tur adipiscing elied do.</p><div class="foot"><span class="dist">Up to <b>2</b> km</span><a class="btn" href="#">LEARN MORE</a></div></article>
  <article class="card"><div class="ph t-grey" role="img" aria-label="Resort buildings with rounded balconies"></div><h3>Ancient dome tomb</h3><p>Lorem ipsum dolor sit amet, cons ecte tur adipiscing elied do.</p><div class="foot"><span class="dist">Up to <b>2</b> km</span><a class="btn" href="#">LEARN MORE</a></div></article>
  <article class="card"><div class="ph t-night" role="img" aria-label="Resort gardens lit up in the evening"></div><h3>Ridgeway Winery</h3><p>Lorem ipsum dolor sit amet, cons ecte tur adipiscing elied do.</p><div class="foot"><span class="dist">Up to <b>2</b> km</span><a class="btn" href="#">LEARN MORE</a></div></article>
</section>

<footer class="site-footer">
  <div class="f-brand"><span class="brand-mark"></span><span class="brand-name">Duskfall Resort</span></div>
  <ul class="f-contact">
    <li><svg viewBox="0 0 24 24"><path d="M12 2a7 7 0 00-7 7c0 5 7 13 7 13s7-8 7-13a7 7 0 00-7-7zm0 9.5a2.5 2.5 0 110-5 2.5 2.5 0 010 5z"/></svg><span>Duskfall Resort, 14 Harbour Lane<br>St. 4417 Saltmere, Coastland</span></li>
    <li><svg viewBox="0 0 24 24"><path d="M6.6 10.8a15 15 0 006.6 6.6l2.2-2.2c.3-.3.7-.4 1-.2 1.1.4 2.3.6 3.6.6.6 0 1 .4 1 1V20c0 .6-.4 1-1 1A17 17 0 013 4c0-.6.4-1 1-1h3.5c.6 0 1 .4 1 1 0 1.3.2 2.5.6 3.6.1.3 0 .7-.2 1z"/></svg><span>+990 500 123 45</span></li>
    <li><svg viewBox="0 0 24 24"><path d="M2 5h20v14H2zm2 2v.5l8 5 8-5V7z"/></svg><span>stay@duskfallresort.example</span></li>
  </ul>
  <div class="f-col" style="left:457px">
    <h4>Quick Links</h4>
    <ul><li>Contact</li><li>Hotel Fact Sheet</li><li>Prices</li><li>360® VR</li><li>Awards</li><li>Stay Safe Organizer</li><li>Company details</li><li>FAQ</li></ul>
  </div>
  <div class="f-col legal" style="left:842px">
    <h4>Legal</h4>
    <ul><li>Terms</li><li>Disclaimer</li><li>Privacy Policy</li></ul>
  </div>
  <div class="rule"></div>
  <p class="copy">Copyright © 2021, Duskfall Resort. All rights reserved.</p>
  <div class="social" aria-label="Social links">
    <span></span><span></span><span></span><span></span><span></span><span></span>
  </div>
</footer>
</body>
</html>
```